A clean crisp business card for a Landscape Construction company. Designed to be easy to read contact/ info and also be appealing/interesting, unlike a traditional business card.

Industry/Entity Type

Landscape Construction

Contact Information for Business Card

Company name : Bramblecrest Landscape Construction, phone number: (877) 62Vales, website:Bramblecrestlandscapes.example, Email, sales@bramblecrestlandscapes.example

Requirements
Nice to have
• Luxurious finishes/ details…. Icons or emblems next to contact info
Should not have
• Clipart or general pictures

```html
<!DOCTYPE html>
<html lang="en">
<head>
<meta charset="utf-8">
<title>Bramblecrest Landscape Construction – Business Card Concepts</title>
<link rel="stylesheet" href="https://fonts.googleapis.com/css2?family=Cinzel:wght@600;700&family=Jost:wght@400&family=Exo+2:wght@800&display=swap">
<style>
  :root {
    --ink: #000000;
    --paper: #ffffff;
    --brand-blue: #1f63c6;
    --brand-green: #8cc63f;
    --line-grey: #8a8a8a;
    --skyline-dark: #2b2b2b;
    --skyline-light: #d6d6d6;
    --skyline-strong: #a9a9a9;
  }
  * { margin: 0; padding: 0; box-sizing: border-box; }
  html, body { width: 1200px; height: 719px; overflow: hidden; background: var(--paper); }
  .board {
    position: relative;
    width: 1200px; height: 719px;
    background: var(--paper);
    border: 2px solid var(--ink);
  }
  .brand-mark {
    position: absolute; left: 96px; top: 86px;
    display: flex; align-items: center; gap: 8px;
    font-family: "Cinzel", serif; font-weight: 700;
    color: var(--brand-blue);
  }
  .brand-mark .dot { width: 14px; height: 14px; border-radius: 50%; background: var(--brand-green); }
  .brand-mark .name { font-size: 17px; line-height: 1.15; }
  .brand-mark .name small { display: block; font-size: 8.5px; letter-spacing: 1.2px; }
  .board-title {
    position: absolute; right: 105px; top: 82px;
    text-align: right;
    font-family: "Exo 2", sans-serif; font-weight: 800;
    font-size: 19px; line-height: 23px; letter-spacing: 1.6px;
    color: var(--ink);
  }
  .card {
    position: absolute; top: 188px;
    width: 250px; height: 460px;
    overflow: hidden;
    border-radius: 3px;
  }
  .card--dark { background: var(--ink); color: var(--paper); }
  .card--light { background: var(--paper); color: var(--ink); border: 1px solid var(--line-grey); }
  .card--front-dark { left: 67px; }
  .card--back-dark { left: 337px; }
  .card--front-light { left: 612px; }
  .card--back-light { left: 882px; }

  .card-brand {
    position: absolute; left: 0; right: 0; top: 258px;
    text-align: center;
    font-family: "Cinzel", serif; font-weight: 600;
  }
  .card-brand .dot {
    display: block; width: 26px; height: 26px; margin: 0 auto 10px;
    border-radius: 50%; background: currentColor;
  }
  .card-brand .name { font-size: 16px; letter-spacing: 0.5px; line-height: 1.1; }
  .card-brand .tag { display: block; font-size: 7px; letter-spacing: 1.5px; margin-top: 3px; }
  .card-front .card-brand { top: 56px; }

  .person {
    position: absolute; left: 40px; top: 72px;
    font-family: "Cinzel", serif; font-weight: 700;
  }
  .person .name { font-size: 19px; line-height: 22px; letter-spacing: 0.3px; }
  .person .role { font-family: "Cinzel", serif; font-weight: 600; font-size: 12px; letter-spacing: 0.6px; margin-top: 1px; }

  .contacts {
    position: absolute; left: 38px; top: 191px;
    list-style: none;
    font-family: "Jost", sans-serif; font-weight: 400; font-size: 10.5px;
  }
  .contacts li { display: flex; align-items: center; gap: 8px; height: 17px; white-space: nowrap; }
  .contacts svg { width: 11px; height: 11px; flex: none; }

  .skyline { position: absolute; left: 0; right: 0; bottom: 0; }
  .skyline--tall { top: 189px; }
  .skyline--short { top: 311px; }
  .card--dark .skyline { background: linear-gradient(180deg, var(--ink) 0%, var(--skyline-dark) 100%); }
  .card--front-light .skyline { background: linear-gradient(180deg, var(--paper) 0%, var(--skyline-light) 100%); }
  .card--back-light .skyline { background: linear-gradient(180deg, var(--paper) 0%, var(--skyline-strong) 100%); }
</style>
</head>
<body>
<main class="board">
  <div class="brand-mark">
    <span class="dot"></span>
    <span class="name">Bramblecrest<small>LANDSCAPE CONSTRUCTION</small></span>
  </div>
  <h1 class="board-title">BUSINESS CARD<br>CONCEPTS</h1>

  <!-- Dark front -->
  <section class="card card--dark card--front-dark card-front">
    <div class="card-brand">
      <span class="dot"></span>
      <div class="name">BRAMBLECREST</div>
      <span class="tag">LANDSCAPE CONSTRUCTION</span>
    </div>
    <div class="skyline skyline--tall" role="img" aria-label="Line drawing of a city skyline with office towers and trees"></div>
  </section>

  <!-- Dark back -->
  <section class="card card--dark card--back-dark">
    <div class="person">
      <div class="name">MATHÉO BRÜNWALD</div>
      <div class="role">LEAD ENGINEER</div>
    </div>
    <ul class="contacts">
      <li><svg viewBox="0 0 12 12" fill="none" stroke="currentColor" stroke-width="1"><path d="M2.5 1.5l2 2-1 1.2a6 6 0 0 0 3.8 3.8l1.2-1 2 2-1.2 1.2C5.5 10.5 1.5 6.5 1.3 2.7z"/></svg>877 62 Vales</li>
      <li><svg viewBox="0 0 12 12" fill="none" stroke="currentColor" stroke-width="1"><circle cx="6" cy="6" r="5"/><ellipse cx="6" cy="6" rx="2.2" ry="5"/><path d="M1 6h10M2 3.5h8M2 8.5h8"/></svg>sales@bramblecrestlandscapes.example</li>
      <li><svg viewBox="0 0 12 12" fill="none" stroke="currentColor" stroke-width="1"><rect x="1" y="2.5" width="10" height="7"/><path d="M1 2.5l5 4 5-4M1 9.5l3.5-3.5M11 9.5L7.5 6"/></svg>www.bramblecrestlandscapes.example</li>
    </ul>
    <div class="skyline skyline--short" role="img" aria-label="Line drawing of city towers"></div>
  </section>

  <!-- Light front -->
  <section class="card card--light card--front-light card-front">
    <div class="card-brand">
      <span class="dot"></span>
      <div class="name">BRAMBLECREST</div>
      <span class="tag">LANDSCAPE CONSTRUCTION</span>
    </div>
    <div class="skyline skyline--tall" role="img" aria-label="Grey line drawing of a city skyline with office towers and trees"></div>
  </section>

  <!-- Light back -->
  <section class="card card--light card--back-light">
    <div class="person">
      <div class="name">MATHÉO BRÜNWALD</div>
      <div class="role">LEAD ENGINEER</div>
    </div>
    <ul class="contacts">
      <li><svg viewBox="0 0 12 12" fill="none" stroke="currentColor" stroke-width="1"><path d="M2.5 1.5l2 2-1 1.2a6 6 0 0 0 3.8 3.8l1.2-1 2 2-1.2 1.2C5.5 10.5 1.5 6.5 1.3 2.7z"/></svg>877 62 Vales</li>
      <li><svg viewBox="0 0 12 12" fill="none" stroke="currentColor" stroke-width="1"><circle cx="6" cy="6" r="5"/><ellipse cx="6" cy="6" rx="2.2" ry="5"/><path d="M1 6h10M2 3.5h8M2 8.5h8"/></svg>sales@bramblecrestlandscapes.example</li>
      <li><svg viewBox="0 0 12 12" fill="none" stroke="currentColor" stroke-width="1"><rect x="1" y="2.5" width="10" height="7"/><path d="M1 2.5l5 4 5-4M1 9.5l3.5-3.5M11 9.5L7.5 6"/></svg>www.bramblecrestlandscapes.example</li>
    </ul>
    <div class="skyline skyline--short" role="img" aria-label="Black line drawing of city towers"></div>
  </section>
</main>
</body>
</html>
```